Retail and Ecommerce Archery Shop needs new Home Page Design

We need a homepage design created for an existing company named Harlow Ridge Sport Depot. They sell various types of Archery equipment for both Bow hunting and Target shooting both in store and online. They offer shooting lessons, have an indoor archery shooting range with memberships available, and have their own line of bowstrings. For color scheme, use the current home page as inspiration. The Homepage Template has links to specific images, if any other images are needed, stock images are acceptable.

Current Website: https://hrsportdepot.com/

Customer Avatar: https://files.norvexa.com/doc/d/7Tq2Wm9XbR4LpZ8vKc3NhY6JfG1sDe5AaUoPiQwErTy/view?mode=share

Core Message Canvas: https://files.norvexa.com/sheet/d/4K_718bnRz962T3w57nLqX8hjd4Mc2Vb7wP0gE3R_uHz/view?mode=share

Homepage Template-Use this worksheet as the structue of the homepage: https://files.norvexa.com/doc/d/9pLxTrWq2N8mHc4ZbVs5KdYo7GfEjU3RaCiAwB6nMeQ/view?mode=share

```html
<!DOCTYPE html>
<html lang="en">
<head>
<meta charset="utf-8">
<title>Harlow Ridge Sport Depot — Home</title>
<link href="https://fonts.googleapis.com/css2?family=Fira+Sans:wght@500;600&family=Inter:wght@400;500&display=swap" rel="stylesheet">
<style>
:root{
  --black:#000;
  --ink:#1f1f1f;
  --grey:#6b6b6b;
  --line:#bdbdbd;
  --red:#ee1c25;
  --white:#fff;
  --panel:rgba(20,20,20,.78);
  --gold:#f2c200;
}
*{box-sizing:border-box;margin:0;padding:0}
html,body{width:1200px;height:3429px;overflow:hidden;background:var(--white);font-family:'Inter',sans-serif;color:var(--ink)}
.page{position:relative;width:1200px;height:3429px}
.abs{position:absolute}
.center{left:0;width:1200px;text-align:center}
.btn{position:absolute;background:var(--red);color:var(--white);display:flex;align-items:center;justify-content:center;gap:10px;font-size:15px;box-shadow:0 2px 4px rgba(0,0,0,.25)}
.btn svg{width:14px;height:14px}

/* nav */
.topbar{left:0;top:0;width:1200px;height:60px;background:var(--black)}
.brand{left:36px;top:18px;color:var(--gold);font-family:'Fira Sans',sans-serif;font-weight:600;font-size:15px;display:flex;align-items:center;gap:6px}
.brand .dot{width:10px;height:10px;background:var(--red);border-radius:50%}
.nav a{position:absolute;top:22px;color:var(--white);font-size:14px;text-decoration:none}

/* hero */
.hero{left:0;top:60px;width:1200px;height:540px;background:radial-gradient(ellipse at 40% 40%,#4a4238 0%,#2b2822 45%,#161412 100%)}
.search{left:877px;top:80px;width:275px;height:34px;background:#3a3a3a;border:1px solid #555;color:#bbb;font-size:10px;padding:11px 12px}
.search svg{position:absolute;right:10px;top:10px}
.hero-title{top:136px;font-family:'Fira Sans',sans-serif;font-weight:600;font-size:38px;color:var(--white)}
.features{left:276px;top:226px;width:647px;height:174px;background:var(--panel)}
.feature{position:absolute;top:30px;width:200px;text-align:center;color:var(--white);font-size:12px}
.feature svg{display:block;margin:0 auto 14px}

/* services */
.h2{font-size:28px;color:var(--ink)}
.lede{font-size:13px;line-height:17px;color:#333}
.partner{position:absolute;top:890px;height:50px;width:110px;background:#d9d9d9;border-radius:25px}
.rule{position:absolute;height:1px;background:var(--line)}

/* video */
.video-band{left:0;top:1140px;width:1200px;height:723px;background:#111}
.video{left:0;top:1285px;width:1200px;height:418px;background:linear-gradient(90deg,#3a3a3d 0%,#2a2c33 45%,#23252c 70%,#3a3632 100%)}
.video-title{top:1204px;font-size:24px;color:var(--white)}

/* welcome */
.q{font-size:20px;color:var(--ink)}
.qp{font-size:15px;line-height:19px;color:var(--grey)}

/* newsletter */
.news{left:0;top:2700px;width:1200px;height:362px;background:linear-gradient(180deg,#9a9a9a,#8a8a8a 60%,#999)}
.news-title{top:2765px;font-size:28px;color:#1a1a1a}
.news-sub{top:2828px;font-size:18px;color:#2a2a2a}
.form{left:177px;top:2918px;width:840px;height:60px;background:var(--white);box-shadow:0 3px 6px rgba(0,0,0,.3)}
.form span{position:absolute;left:20px;top:21px;font-size:15px;color:#777}

/* footer */
.footer{left:0;top:3248px;width:1200px;height:181px;background:var(--black);color:var(--white)}
.foot-brand{left:78px;top:3306px;color:var(--gold);font-family:'Fira Sans',sans-serif;font-weight:600;font-size:24px;display:flex;align-items:center;gap:8px}
.foot-brand .dot{width:14px;height:14px;background:var(--red);border-radius:50%}
.foot-nav a{position:absolute;top:3276px;color:var(--white);font-size:13px;text-decoration:none}
.legal a{position:absolute;top:3339px;font-size:9px;color:#aaa;text-decoration:underline}
.copy{top:3390px;font-size:6px;color:#777}
.contact h4{position:absolute;left:952px;top:3276px;font-weight:400;font-size:13px}
.contact p{position:absolute;left:978px;font-size:8px;color:#ccc}
.contact svg{position:absolute;left:954px}
</style>
</head>
<body>
<div class="page">

  <header class="abs topbar"></header>
  <div class="abs brand"><span class="dot"></span>Harlow Ridge</div>
  <nav class="nav">
    <a style="left:650px">Shop</a>
    <a style="left:726px">About Us</a>
    <a style="left:828px">Range</a>
    <a style="left:913px">Pro Shop</a>
    <a style="left:1022px">Electric Bowstrings</a>
  </nav>

  <section class="abs hero" role="img" aria-label="Bow hunter drawing a bow in a dim woodland with wildflowers"></section>
  <div class="abs search">Search items
    <svg width="13" height="13" viewBox="0 0 14 14" fill="none" stroke="#aaa" stroke-width="1.4"><circle cx="6" cy="6" r="4.5"/><path d="M9.5 9.5L13 13"/></svg>
  </div>
  <h1 class="abs center hero-title">Your Bow Hunting Adventure Starts Here!</h1>
  <div class="abs features">
    <div class="feature" style="left:14px">
      <svg width="60" height="60" viewBox="0 0 60 60" fill="none" stroke="#ee1c25" stroke-width="4"><path d="M12 10 Q50 10 50 48"/><path d="M12 10 L50 48" stroke-width="2"/><path d="M8 52 L44 16"/><path d="M44 16 l-8 1 m8 -1 l-1 8" /></svg>
      Top-Notch Equipment
    </div>
    <div class="feature" style="left:231px">
      <svg width="60" height="60" viewBox="0 0 60 60"><path d="M30 12 L46 20 L46 40 L30 50 L14 40 L14 20Z" fill="#ee1c25"/><circle cx="30" cy="31" r="12" fill="none" stroke="#1a1a1a" stroke-width="2"/><path d="M30 2l2 4 4 .5-3 3 1 4-4-2-4 2 1-4-3-3 4-.5z M14 6l2 3 3 .5-2 2 .5 3-3.5-1.5-3 1.5.5-3-2-2 3-.5z M46 6l2 3 3 .5-2 2 .5 3-3.5-1.5-3 1.5.5-3-2-2 3-.5z" fill="#ee1c25"/></svg>
      Expertise
    </div>
    <div class="feature" style="left:438px">
      <svg width="60" height="60" viewBox="0 0 60 60" fill="#ee1c25"><circle cx="16" cy="14" r="7"/><path d="M5 26h22v12h-6v16H11V38H5z"/><path d="M30 34h6l4-10h4v10h8v18H30z"/><path d="M44 4l5 5-5 5-5-5z M54 16l4 4-4 4-4-4z"/></svg>
      Unmatched Support
    </div>
  </div>
  <a class="btn" style="left:349px;top:475px;width:209px;height:46px">Indoor Archery Range !!</a>
  <a class="btn" style="left:642px;top:475px;width:208px;height:46px">Shop Our Bows
    <svg viewBox="0 0 14 14" fill="none" stroke="#fff" stroke-width="1.5"><path d="M1 7h11M8 3l4 4-4 4"/></svg></a>

  <h2 class="abs center h2" style="top:722px">We Are a Full-Service Archery Pro Shop</h2>
  <p class="abs lede" style="left:190px;width:820px;top:785px;text-align:center">Our services include Bow setup and sizing, D-loop and peep sight installs, accessory installs, and setup, cam/limb swaps, string swaps, paper tuning, 2nd/3rd axis adjustments, replacement parts, arrow building, tuning, and much more!</p>
  <div class="partner" style="left:100px;width:80px"></div>
  <div class="partner" style="left:259px"></div>
  <div class="partner" style="left:455px"></div>
  <div class="partner" style="left:642px"></div>
  <div class="partner" style="left:825px"></div>
  <div class="partner" style="left:1006px;width:94px;border-radius:50%"></div>
  <div class="rule" style="left:287px;top:1000px;width:625px"></div>

  <section class="abs video-band"></section>
  <h2 class="abs center video-title">Our Custom Electric Bowstrings</h2>
  <div class="abs video" role="img" aria-label="Video still: archer drawing a compound bow in the shop while a technician watches"></div>
  <svg class="abs" style="left:553px;top:1449px" width="94" height="94" viewBox="0 0 94 94" fill="none"><circle cx="47" cy="47" r="43" stroke="rgba(255,255,255,.45)" stroke-width="5"/><path d="M38 28 L64 47 L38 66Z" fill="rgba(255,255,255,.45)"/></svg>
  <a class="btn" style="left:431px;top:1762px;width:338px;height:48px;font-size:19px">Shop Our Custom Bowstrings
    <svg viewBox="0 0 14 14" fill="none" stroke="#fff" stroke-width="1.5"><path d="M1 7h11M8 3l4 4-4 4"/></svg></a>

  <h2 class="abs center h2" style="top:1942px">Welcome to your local Archery Shop</h2>
  <p class="abs center" style="top:1998px;font-size:19px;color:var(--grey)">[Where consistency is built]</p>

  <h3 class="abs center q" style="top:2101px">Looking for a new Bow setup?</h3>
  <p class="abs qp" style="left:190px;width:820px;top:2146px;text-align:center">Our custom bow-fitting process will be perfect for you. We get you set up the right way, the first time! We will get your measurements, check your shot, and make sure you leave feeling confident with your new Bow!</p>
  <div class="rule" style="left:407px;top:2205px;width:430px"></div>

  <h3 class="abs center q" style="top:2252px">Looking to make some improvements to your current archery setup?</h3>
  <p class="abs qp" style="left:190px;width:820px;top:2297px;text-align:center">We have access to almost all of the popular archery accessories on the market! We don't sell anything we wouldn't use ourselves so come on in and talk with our shop experts to figure out what will work best for you.</p>
  <div class="rule" style="left:409px;top:2355px;width:430px"></div>

  <h3 class="abs center q" style="top:2403px">Are you looking to improve your shot? Reserve some time on our range!</h3>
  <p class="abs qp" style="left:188px;width:824px;top:2448px;text-align:center">Before you step into the field to take your first shot of the season, take time to go to the range. Archery, like any skill, requires practice &amp; diligence to develop a consistent &amp; confident shot. We have a 12-lane 20-yard indoor range in the shop. Daily Range and memberships are available. We also offer bow rental and lessons.</p>
  <div class="rule" style="left:420px;top:2525px;width:430px"></div>
  <a class="btn" style="left:495px;top:2591px;width:210px;height:43px">Range Information
    <svg viewBox="0 0 14 14" fill="none" stroke="#fff" stroke-width="1.5"><path d="M1 7h11M8 3l4 4-4 4"/></svg></a>

  <section class="abs news" role="img" aria-label="Faded photo of a busy archery trade show floor"></section>
  <h2 class="abs center news-title">[Join Our Archery Community: Exclusive Deals, Tips, and Updates Straight to Your Inbox!]</h2>
  <p class="abs center news-sub">[Join today &amp; stay up-to-date on new product releases, shop promotions, and our archery newsletters]</p>
  <div class="abs form"><span>Enter your Email here...</span></div>
  <a class="btn" style="left:717px;top:2925px;width:295px;height:45px;box-shadow:none">Subscribe Now !!</a>

  <footer class="abs footer"></footer>
  <div class="abs foot-brand"><span class="dot"></span>Harlow Ridge Sport Depot</div>
  <nav class="foot-nav">
    <a style="left:385px">Shop</a>
    <a style="left:444px">About Us</a>
    <a style="left:529px">Range</a>
    <a style="left:591px">Pro Shop</a>
    <a style="left:680px">Electric Bowstrings</a>
  </nav>
  <div class="legal">
    <a style="left:514px">Terms Of Service</a>
    <span class="abs" style="left:604px;top:3338px;font-size:9px;color:#aaa">|</span>
    <a style="left:614px">Refund Policy</a>
  </div>
  <p class="abs center copy">© Harlow Ridge Sport Depot LLC 2023</p>
  <div class="contact">
    <h4>Get in touch</h4>
    <svg style="top:3314px" width="10" height="13" viewBox="0 0 10 13" fill="none" stroke="#ccc" stroke-width="1.2"><path d="M5 12S1 7.5 1 5a4 4 0 018 0c0 2.5-4 7-4 7z"/><circle cx="5" cy="5" r="1.5"/></svg>
    <p style="top:3316px">4120 Cedar Bluff Rd, Harlow, KS 67001</p>
    <svg style="top:3345px" width="11" height="11" viewBox="0 0 11 11" fill="#ccc"><path d="M2 0l2 2.5-1.2 1.5a7 7 0 004 4L8.5 6.8 11 9l-1.5 2C4 11 0 7 0 1.5z"/></svg>
    <p style="top:3347px">555-014-2273</p>
    <svg style="top:3376px" width="12" height="9" viewBox="0 0 12 9" fill="none" stroke="#ccc" stroke-width="1.1"><rect x=".5" y=".5" width="11" height="8"/><path d="M.5 .5L6 5l5.5-4.5"/></svg>
    <p style="top:3377px">hello@hrsportdepot.com</p>
  </div>

</div>
</body>
</html>
```